Finance Company Needs a New Website Design

Looking for a fresh new design, based on logo and wireframes given, to come up with a modern professional look and feel for the company. Note we will award based on the homepage design, but expect the winning designer to deliver the other pages.

Target Market(s)

Large Corporate and Finance Professionals (C-Suite Level)

Industry/Entity Type

Finance / Professional

Number of Pages Required

5+ page

Font styles to use
Sans Serif
Other font styles liked:
• Use Roboto/Open Sans for body/small headings, use Impact for larger headings (like the Brevath website).

Requirements
Must have
• High Attention to Detail. Following the Wireframes closely. High impact and fits well with the Brevath.co.uk website.
Nice to have
• Must fit with the Brevath website look and feel, but be different - so that they cannot be mistaken for each other. Use the arrow motif from the logo carefully.
Should not have
• Anything cheap, too bright or untidy

```html
<!DOCTYPE html>
<html lang="en">
<head>
<meta charset="utf-8">
<title>Keyvale – Sell Your Business</title>
<link rel="stylesheet" href="https://fonts.googleapis.com/css2?family=Anton&family=Roboto:wght@300;400;500;700&display=swap">
<style>
:root{
  --yellow:#ffcf00;
  --plum:#51215d;
  --purple:#753f9a;
  --band:#661a70;
  --charcoal:#414141;
  --grey:#666666;
  --paper:#f1f2f3;
  --stage:#e4e4e4;
  --ink:#232323;
  --display:'Anton',Impact,sans-serif;
  --body:'Roboto',Arial,sans-serif;
}
*{box-sizing:border-box;margin:0;padding:0}
html,body{width:1200px;height:4174px;overflow:hidden}
body{background:var(--stage);font-family:var(--body);color:var(--grey);position:relative}

/* style board */
.board-logo{position:absolute;left:198px;top:74px;font:700 40px/1 var(--body);color:var(--plum);letter-spacing:-1px}
.board-fonts{position:absolute;left:556px;top:50px}
.board-title{font:400 26px/1 var(--body);color:#333;margin-bottom:10px}
.board-fonts .f1{font:400 22px/1.2 var(--display);color:#555}
.board-fonts .f2{font:400 18px/1.3 var(--body);color:#888}
.board-colors{position:absolute;left:739px;top:50px}
.swatches{display:flex;gap:12px;margin-top:2px}
.swatch{width:40px;text-align:center;font-size:9px;color:#777}
.swatch i{display:block;width:40px;height:40px;border-radius:50%;margin-bottom:6px}

/* page */
.page{position:absolute;left:222px;top:227px;width:792px;height:3888px;background:#fff;overflow:hidden}
.wrap{margin:0 14px;position:relative}
section{overflow:hidden}

.topbar{height:26px;display:flex;justify-content:flex-end;align-items:center;gap:26px;font-size:6px;color:#888;text-transform:uppercase}
.phone-btn{background:var(--yellow);color:var(--ink);font-weight:700;height:26px;padding:0 12px;display:flex;align-items:center;gap:5px}
.mainbar{height:37px;display:flex;align-items:center;gap:14px}
.logo{font:700 22px/1 var(--body);color:var(--plum);letter-spacing:-.5px}
.mainbar .rule{flex:1;height:1px;background:#ccc}
.mainnav{display:flex;gap:40px;font-size:7px;font-weight:500;color:#555;text-transform:uppercase}

.hero{height:359px;position:relative;background:linear-gradient(180deg,#cfcfcf 0%,#7a7a7a 45%,#2b2b2b 100%)}
.hero h1{position:absolute;top:234px;font:400 39px/1 var(--display);color:#fff;text-transform:uppercase}
.hero .left{left:50px}
.hero .right{right:50px;text-align:right}
.hl{color:var(--yellow)}
.hp{color:var(--purple)}

.h2{font:400 35px/1 var(--display);color:var(--charcoal);text-transform:uppercase}
.copy p{font-size:8.5px;line-height:1.55;margin-bottom:10px}
.copy strong{color:var(--purple);font-weight:500}

.intro{height:313px;padding-top:47px;text-align:center}
.intro .copy{width:390px;margin:16px auto 0}
.intro .copy p{font-size:8px;line-height:1.5;margin-bottom:8px}

.split{display:flex;height:372px}
.split .panel{width:381px;height:372px;flex:none}
.split .text{flex:1;padding-left:50px;padding-top:44px;padding-right:30px}
.split .text .copy{margin-top:22px;width:290px}
.radar{background:radial-gradient(circle at 60% 45%,#8a8a8a 0%,#333 45%,#111 100%)}
.puzzle{background:linear-gradient(135deg,#dcdcdc 0%,#9a9a9a 55%,#3a3a3a 100%)}

.btn{display:inline-flex;align-items:center;height:27px;padding:0 26px 0 18px;font-size:6.5px;font-weight:700;text-transform:uppercase;clip-path:polygon(0 0,100% 0,88% 50%,100% 100%,0 100%)}
.btn.y{background:var(--yellow);color:var(--ink)}
.btn.p{background:var(--plum);color:#fff}
.btn.o{border:1px solid rgba(255,255,255,.5);color:#fff;background:var(--plum)}

.video{height:315px;margin-top:45px;position:relative;background:linear-gradient(90deg,#c9c9c9 0%,#6d6d6d 50%,#c9c9c9 100%);display:flex;flex-direction:column;align-items:center;justify-content:center}
.video h2{font:400 32px/1.1 var(--display);color:#fff;text-transform:uppercase;text-align:center;margin-top:-4px}
.play{width:49px;height:49px;background:var(--plum);display:flex;align-items:center;justify-content:center;margin-top:14px}

.contact{height:228px;text-align:center;padding-top:45px}
.contact p{font-size:8.5px;line-height:1.55;width:400px;margin:16px auto 20px}
.contact .btns{display:flex;gap:14px;justify-content:center}

.valuation{height:368px;background:var(--band);text-align:center;padding-top:46px;position:relative;color:#e7d6ea}
.valuation .h2{color:#fff}
.valuation p{font-size:8.5px;line-height:1.55;width:390px;margin:0 auto 10px}
.valuation .copy{margin-top:22px}
.valuation .line{position:absolute;left:0;right:0;top:257px;height:1px;background:rgba(255,255,255,.25)}
.valuation .btns{position:relative;display:flex;gap:14px;justify-content:center;margin:12px 0 18px}
.valuation strong{color:#fff;font-weight:700}

.articles{padding-top:44px;text-align:center;height:356px}
.cards{display:flex;gap:15px;margin-top:26px}
.card{width:180px;position:relative;height:160px}
.card .img{height:122px;background:linear-gradient(180deg,#e6e6e6,#8c8c8c)}
.card .label{position:absolute;left:14px;right:14px;top:113px;background:#fff;padding:8px 6px;font-size:8.5px;line-height:1.3;color:#444;border-bottom:1px solid #ddd}
.more{font-size:6.5px;color:var(--purple);margin-top:20px}
.divider{height:1px;background:#ccc}

.reach{height:526px;text-align:center;padding-top:48px}
.reach .copy{width:350px;margin:22px auto 0}
.map{width:445px;height:267px;margin:26px auto 0;background:linear-gradient(90deg,#7a2e88 0%,#dcd8e2 45%,#7a2e88 70%,#dcd8e2 100%)}

.offices{height:294px;text-align:center;padding-top:48px}
.offices .lead{font-size:8.5px;line-height:1.55;width:380px;margin:18px auto 26px}
.office-row{display:flex;justify-content:space-between;text-align:left;padding:0 50px 0 65px}
.office{display:flex;gap:14px}
.office h3{font-size:9px;font-weight:500;color:#333;margin-bottom:14px}
.office p{font-size:7.5px;line-height:1.7}
.office .tel{font-size:9px;color:#333;margin-top:10px}
.office .tel b{font-weight:700}
.mini-map{width:130px;height:96px;background:linear-gradient(135deg,#f4f4f4,#dedede)}

.footer{position:absolute;left:14px;right:14px;top:3614px;height:265px;background:var(--ink);color:#bbb}
.footer .cut{position:absolute;right:0;top:0;width:42px;height:82px;background:#fff;clip-path:polygon(100% 0,100% 100%,70% 100%,45% 55%,100% 0)}
.cols{position:absolute;top:48px;left:50px;right:0;display:flex}
.col h4{font-size:10px;font-weight:700;color:#fff;text-transform:uppercase;margin-bottom:16px}
.col li{list-style:none;font-size:7px;line-height:2.3}
.col1{width:208px}.col2{width:162px}.col3{width:175px}
.mail{margin-top:10px;display:inline-flex;align-items:center;gap:5px;background:var(--yellow);color:var(--ink);font-size:6px;font-weight:700;height:22px;padding:0 12px}
.legal{position:absolute;top:210px;left:50px;right:60px;display:flex;justify-content:space-between;font-size:6px;color:#aaa}
</style>
</head>
<body>

<div class="board-logo">keyvale</div>
<div class="board-fonts">
  <div class="board-title">Fonts:</div>
  <div class="f1">Impact</div>
  <div class="f2">Roboto</div>
</div>
<div class="board-colors">
  <div class="board-title">Colors:</div>
  <div class="swatches">
    <div class="swatch"><i style="background:var(--yellow)"></i>#ffcf00</div>
    <div class="swatch"><i style="background:var(--plum)"></i>#51215d</div>
    <div class="swatch"><i style="background:var(--purple)"></i>#753f9a</div>
    <div class="swatch"><i style="background:var(--charcoal)"></i>#414141</div>
    <div class="swatch"><i style="background:var(--grey)"></i>#666666</div>
    <div class="swatch"><i style="background:var(--paper)"></i>#f1f2f3</div>
  </div>
</div>

<main class="page">
  <div class="wrap">
    <div class="topbar">
      <span>Insights &amp; News</span><span>About Us</span><span>Contact</span>
      <span class="phone-btn"><svg width="7" height="7" viewBox="0 0 24 24"><path fill="#232323" d="M6.6 10.8a15 15 0 006.6 6.6l2.2-2.2c.3-.3.7-.4 1-.2 1.1.4 2.3.6 3.6.6.6 0 1 .4 1 1V20c0 .6-.4 1-1 1A17 17 0 013 4c0-.6.4-1 1-1h3.5c.6 0 1 .4 1 1 0 1.3.2 2.5.6 3.6.1.3 0 .7-.2 1z"/></svg>0300 555 0142</span>
    </div>
    <div class="mainbar">
      <span class="logo">keyvale</span><span class="rule"></span>
      <nav class="mainnav"><span>Sell Your Business</span><span>Valuation</span><span>Work With Us</span></nav>
    </div>

    <section class="hero" role="img" aria-label="Black and white photograph of an escalator rising between steel walls">
      <h1 class="left">We <span class="hl">Find</span> the<br>Best Buyer</h1>
      <h1 class="right">You <span class="hl">Get</span> the<br>Best Exit</h1>
    </section>

    <section class="intro">
      <h2 class="h2">Sell Your Business<br><span class="hp">For More</span></h2>
      <div class="copy">
        <p>You may have already considered how much your business is worth, or even have received a suggested price for the sale of your business. If you have, then it might be worth considering a very apparent truth.</p>
        <p>Any business valuation you have in mind or have received, is just a number. In many cases, it is not close to what your business may sell for. To wish is one thing, to receive a good offer is much harder.</p>
        <p>Which is why owners choose to work with us. We know that your future business disposal and sale price will be maximised in two ways: <strong>by reaching as many of the most likely buyers</strong> as possible, and by <strong>finding the best fit</strong>.</p>
        <p>Only then you receive the best offer for your business and complete the disposal of your company.</p>
      </div>
    </section>

    <section class="split">
      <div class="text">
        <h2 class="h2"><span class="hp">Reach</span> Only<br>Serious Acquirers</h2>
        <div class="copy">
          <p>With access to over 13,000 active acquirers throughout our national and global network, all of whom we have qualified to ensure they have the capabilities to make good offers for suitable businesses.</p>
          <p>We have partnerships with websites we have evaluated to give us the greatest possible coverage of any additional buyers who may be interested in your company.</p>
          <p>We have a full set of global business data meaning that we can run intensive campaigns to help you get in front of specific trade buyers, and with our office in Sydney, we cover every time zone.</p>
        </div>
        <span class="btn y" style="margin-top:16px">Reach Matters</span>
      </div>
      <div class="panel radar" role="img" aria-label="Black and white radar screen with a bright sweeping beam"></div>
    </section>

    <section class="split">
      <div class="panel puzzle" role="img" aria-label="Black and white jigsaw puzzle with a rising bar chart and a hand placing the last piece"></div>
      <div class="text">
        <h2 class="h2">Connect With the<br>Best <span class="hp">Fitting</span> Buyers</h2>
        <div class="copy">
          <p>From our research, and having engaged with as many potential acquirers as possible, we will work alongside you to identify the most interesting prospective acquirers and much more than that.</p>
          <p>In most cases, these are the companies with the best fit for your business. It will mean that they will pay a premium for your business because there is more value.</p>
          <p>Working with you, we will coordinate a competitive process, engaging the most suitable acquirers and their advisors, ensuring that the offers made exceed expectations, not just in price, but also in terms of your future.</p>
        </div>
        <span class="btn y" style="margin-top:16px">Finding the Fit</span>
      </div>
    </section>

    <section class="video" role="img" aria-label="Black and white photograph of an open lift with a video play button">
      <h2>How Reach and Fit Deliver<br>the Best Outcome</h2>
      <span class="play"><svg width="14" height="14" viewBox="0 0 10 10"><path d="M2 1l7 4-7 4z" fill="var(--yellow)"/></svg></span>
    </section>

    <section class="contact">
      <h2 class="h2">Contact the <span class="hp">Keyvale</span> Team</h2>
      <p>Book an introductory call with one of our team and discover first hand how Keyvale can realise a successful sale of your company.</p>
      <div class="btns"><span class="btn y">Call 0300 555 0142</span><span class="btn p">Contact Keyvale</span></div>
    </section>

    <section class="valuation">
      <h2 class="h2">Business Valuations Based<br>on <span class="hl">Real</span> Transcation Data</h2>
      <div class="copy">
        <p>Business valuation is the most misunderstood part of the disposal process and often comes before engaging an advisor. Yet, at this stage it can raise more questions. Why be distracted by hope or hearsay when there is so much information available?</p>
        <p>We have been directly involved in a wide range of transactions, and have also access to deal data from over 1,000 recent business disposals. So we are confident that we have access to enough information to give a more representative view on valuation.</p>
      </div>
      <div class="line"></div>
      <div class="btns"><span class="btn o">V. Calculator</span><span class="btn y">Business Data</span></div>
      <p>So, you can browse our <strong>statistics on valuation</strong> to give a much clearer picture of business value, or use our calculator to get an idea of a starting point for your business value.</p>
    </section>

    <section class="articles">
      <h2 class="h2">Articles <span class="hp">&amp;</span> Insights</h2>
      <div class="cards">
        <div class="card"><div class="img" role="img" aria-label="Stacked blocks forming a staircase"></div><div class="label">You Can Pursue Your Own Business Sale</div></div>
        <div class="card"><div class="img" role="img" aria-label="Paper maze with a paper plane"></div><div class="label">Gain a Full Understanding of What Your Sale Advisor Offers</div></div>
        <div class="card"><div class="img" role="img" aria-label="Hot air balloon in a cloudy sky"></div><div class="label">It's too Easy to Believe the Largest Figure</div></div>
        <div class="card"><div class="img" role="img" aria-label="Person walking up concrete steps"></div><div class="label">Don't Be Your Own Worst Enemy</div></div>
      </div>
      <div class="more">More Insights &amp; News</div>
    </section>

    <div class="divider"></div>

    <section class="reach">
      <h2 class="h2">Local and <span class="hp">International</span> Reach</h2>
      <div class="copy">
        <p>Our focus on technology, business data and modern communications sets us apart. Borders and languages aren't boundaries for the way we operate.</p>
        <p>Our methods are successful whether helping a company sell within a small region, or cross-border or even cross-continent.</p>
      </div>
      <div class="map" role="img" aria-label="World map with covered regions in purple and others in light grey"></div>
    </section>

    <div class="divider"></div>

    <section class="offices">
      <h2 class="h2">Offices</h2>
      <p class="lead">Our two offices are strategically situated in the UK and Australia giving us global coverage and at least one office open at any time of the day or night anywhere in the world.</p>
      <div class="office-row">
        <div class="office">
          <div>
            <h3>UK &amp; Europe Office</h3>
            <p>Fourth Floor<br>Kestrel Court House<br>Thamesford<br>TF4 2QX</p>
            <p class="tel"><b>Contact:</b>+44 (0) 1632 960 418</p>
          </div>
          <div class="mini-map" role="img" aria-label="Street map around the UK office"></div>
        </div>
        <div class="office">
          <div class="mini-map" role="img" aria-label="Street map around the APAC office"></div>
          <div>
            <h3>APAC OFFICE</h3>
            <p>18 Harbourline Street<br>Wattle Quay<br>NSW 2999<br>Australia</p>
            <p class="tel"><b>Contact:</b>+61 (0) 491 570 226</p>
          </div>
        </div>
      </div>
    </section>
  </div>

  <footer class="footer">
    <div class="cut"></div>
    <div class="cols">
      <div class="col col1"><h4>Sell Your Business</h4><ul><li>Direct to Market</li><li>Maximising Reach</li><li>Focus on Fit</li><li>Exit Planning</li></ul></div>
      <div class="col col2"><h4>Valuation</h4><ul><li>Calculator</li><li>Getting the Fit</li><li>How to Build Value</li></ul></div>
      <div class="col col3"><h4>Work With Us</h4><ul><li>M&amp;A Advisors</li><li>Global Coverage</li><li>Acquisitions</li></ul></div>
      <div class="col"><h4>About Us</h4><ul><li>Insights &amp; News</li><li>About Us</li><li>Contact Us</li></ul>
        <span class="mail"><svg width="8" height="6" viewBox="0 0 8 6"><rect width="8" height="6" fill="#232323"/><path d="M0 0l4 3 4-3" stroke="#ffcf00" fill="none" stroke-width=".8"/></svg>Email Us</span></div>
    </div>
    <div class="legal"><span>(C) 2023 Keyvale a Trading Name of Brevath Limited. All Rights Reserved</span><span>Sitemap | Terms of Use | Privacy Policy | Contact Us</span></div>
  </footer>
</main>

</body>
</html>
```